Anzeigengestaltung für ambulanten Pflegedienst
Zielgruppe
Es handelt sich um einen ambulanten Pflegedienst, der am 01. September 2024 einjähriges Jubiläum feiert. Von 10:00 Uhr bis 15:00 Uhr ist dazu im Büro in der Lindenweg 14 in Dessau-Roßlau ein kleiner Empfang mit Kuchen und Getränken geplant.
Weiterhin benötige ich eine Anzeige, um einen Hauswirtschafter zu suchen.
Und eine Anzeige für Beratungen gem.

```html
<!DOCTYPE html>
<html lang="de">
<head>
<meta charset="utf-8">
<title>Auenblick Pflege – Anzeigen</title>
<link href="https://fonts.googleapis.com/css2?family=Crimson+Pro:wght@400&family=Quicksand:wght@500;600;700&display=swap" rel="stylesheet">
<style>
  :root{
    --page:#ffffff;
    --ink:#555759;
    --ink-strong:#4a4c4e;
    --teal:#3aa9a0;
    --green:#6cab2c;
    --band:#ddeef9;
    --ring:#dcdcdc;
    --photo-light:#f1f0ee;
    --photo-mid:#c9d6d2;
    --photo-warm:#d8c2ae;
  }
  *{margin:0;padding:0;box-sizing:border-box}
  html,body{width:1200px;height:846px;overflow:hidden;background:var(--page)}
  body{position:relative;font-family:'Quicksand',sans-serif;color:var(--ink)}

  .ad{position:absolute;top:204px;width:512px;height:398px;background:#fff;overflow:hidden;
      box-shadow:0 1px 6px rgba(0,0,0,.14)}
  .ad--jubilee{left:60px}
  .ad--hiring{left:612px}

  .ad__photo{position:absolute;top:0}
  .ad--jubilee .ad__photo{left:312px;width:380px;height:380px;top:-20px;border-radius:50%;
      background:radial-gradient(circle at 35% 50%,var(--photo-mid),#e7ecea 55%,var(--photo-light))}
  .ad--hiring .ad__photo{left:312px;width:200px;height:340px;
      background:linear-gradient(90deg,#ffffff 0%,#efe9e3 25%,var(--photo-warm) 60%,#b9d3cd 100%)}

  .brand{position:absolute;top:19px;width:98px;height:98px;border-radius:50%;background:#fff;
      border:1.5px solid var(--ring);display:flex;align-items:center;justify-content:center;text-align:center;
      font-weight:600;font-size:11.5px;line-height:1.25;color:var(--ink-strong)}
  .ad--jubilee .brand{left:270px}
  .ad--hiring .brand{left:266px}

  .ad__body{position:absolute;left:39px;top:0;width:280px}
  .kicker{position:absolute;top:36px;font-family:'Crimson Pro',serif;font-size:17.5px;color:var(--ink-strong);white-space:nowrap}
  .headline{position:absolute;top:61px;font-size:19px;font-weight:700;line-height:23px;color:var(--ink-strong);white-space:nowrap}
  .headline__accent{color:var(--teal)}
  .ad--hiring .headline{color:var(--teal);font-size:20.5px}
  .rule{position:absolute;left:0;width:72px;height:3px;background:var(--green)}
  .ad--jubilee .rule{top:118px}
  .ad--hiring .rule{top:95px}

  .lead{position:absolute;font-size:13.5px;font-weight:500;line-height:18px;white-space:nowrap}
  .lead strong{font-weight:700;color:var(--ink-strong)}
  .ad--jubilee .lead{top:134px}
  .ad--hiring .lead{top:110px;font-size:12.3px;line-height:17.5px}

  .section-title{position:absolute;color:var(--green);font-weight:600;white-space:nowrap}
  .ad--jubilee .section-title{top:216px;font-size:14.5px}
  .ad--hiring .section-title{font-size:12.5px}
  .ad--hiring .section-title--needs{top:173px}
  .ad--hiring .section-title--offers{top:255px}

  .list{position:absolute;list-style:none;white-space:nowrap}
  .list li{position:relative;padding-left:15px}
  .list li::before{content:"+";position:absolute;left:0;color:var(--green);font-weight:700}
  .ad--jubilee .list{top:239px;font-size:13.5px;line-height:21.5px}
  .ad--hiring .list{font-size:12.3px;line-height:17.7px}
  .ad--hiring .list--needs{top:189px}
  .ad--hiring .list--offers{top:271px}

  .footer{position:absolute;left:0;bottom:0;width:100%;height:58px;background:var(--band);
      display:flex;align-items:center;justify-content:space-between}
  .footer__note{font-family:'Crimson Pro',serif;color:var(--ink-strong)}
  .ad--jubilee .footer{padding:0 39px 0 32px}
  .ad--jubilee .footer__note{font-size:17px}
  .ad--hiring .footer{padding:0 39px 0 38px}
  .ad--hiring .footer__note{font-size:14px}
  .cta{display:block;height:28px;line-height:28px;border-radius:14px;background:var(--teal);color:#fff;
      font-weight:700;text-align:center;text-decoration:none;white-space:nowrap}
  .ad--jubilee .cta{width:184px;font-size:13.5px}
  .ad--hiring .cta{width:214px;font-size:11.6px}
</style>
</head>
<body>

<article class="ad ad--jubilee">
  <div class="ad__photo" role="img" aria-label="Foto: Pflegekraft in türkisfarbener Kleidung mit einer älteren Patientin"></div>
  <div class="brand">AUENBLICK<br>PFLEGE</div>

  <div class="ad__body">
    <p class="kicker">Feiern Sie mit uns!</p>
    <h2 class="headline">1-jähriges Jubiläum<br><span class="headline__accent">am 01. September 2024</span></h2>
    <span class="rule"></span>
    <p class="lead">Anlässig unseres 1-jährigen Jubiläums,<br>möchten wir uns bei allen <strong>Patienten,</strong><br><strong>Angehörigen und Interessenten</strong> für<br>das Vertrauen bedanken.</p>
    <h3 class="section-title">Besuchen Sie uns:</h3>
    <ul class="list">
      <li>01. Septemer 2024, 10:00 Uhr – 15:00</li>
      <li>Lindenweg 14, Dessau-Roßlau</li>
      <li>Empfang mit Kaffee und Kuchen</li>
      <li>Kostenlose Beratung vor Ort</li>
    </ul>
  </div>

  <footer class="footer">
    <span class="footer__note">Wir freuen uns auf dich!</span>
    <a class="cta" href="#">www.auenblick-pflege.de</a>
  </footer>
</article>

<article class="ad ad--hiring">
  <div class="ad__photo" role="img" aria-label="Foto: lächelnde Hauswirtschafterin mit Schürze, Handschuhen und Sprühflasche"></div>
  <div class="brand">AUENBLICK<br>PFLEGE</div>

  <div class="ad__body">
    <p class="kicker">Komm in unser Team!</p>
    <h2 class="headline">Hauswirtschafter/in</h2>
    <span class="rule"></span>
    <p class="lead">Hilf uns die Pflege in der Umgebung<br>Dessau-Roßlau qualitativ zu verbessern<br>und menschlicher zu gestalten.</p>
    <h3 class="section-title section-title--needs">Was bringst du mit</h3>
    <ul class="list list--needs">
      <li>Hilfsbereitschaft &amp; Engagement</li>
      <li>Führerschein Klasse B</li>
      <li>Gute Deutschkenntnisse in Wort und Schrift</li>
    </ul>
    <h3 class="section-title section-title--offers">Das bieten wir</h3>
    <ul class="list list--offers">
      <li>30 Tage Urlaub</li>
      <li>Fort- &amp; Weiterbildungen, Sonderleistungen</li>
      <li>Überdurchschnittliche Vergütung</li>
    </ul>
  </div>

  <footer class="footer">
    <span class="footer__note">Wir freuen uns auf deine Bewerbung!</span>
    <a class="cta" href="#">www.auenblick-pflege.de/karriere</a>
  </footer>
</article>

</body>
</html>
```